Letterhead and Biz card using my logo
Law Offices of Daniel R. Horvath
Letterhead and Biz card using my logo  - Law
Creative Brief
Professional
The Law Offices of Daniel R. Horvath
41756 County Lane 9 Suite 200 Boca Raton, FL 33517
danielrhorvath@quillpost.net
www.thedebtmender.net
(if you can add this onto the biz card without it looking to busy, use my slogan) "There IS life after bankruptcy."

```html
<!DOCTYPE html>
<html lang="en">
<head>
<meta charset="utf-8">
<title>Daniel R. Horvath – Business Card</title>
<link rel="stylesheet" href="https://fonts.googleapis.com/css2?family=Lato:wght@400;700&display=swap">
<style>
  :root {
    --card-bg: #ffffff;
    --brand-blue: #1d4f9e;
    --brand-blue-light: #3d86d0;
    --swoosh-grey: #8a8d91;
    --swoosh-grey-light: #c9cbce;
    --text-grey: #55585c;
    --name-grey: #5e6166;
  }
  * { margin: 0; padding: 0; box-sizing: border-box; }
  html, body {
    width: 1200px;
    height: 751px;
    overflow: hidden;
    background: var(--card-bg);
  }
  .business-card {
    position: relative;
    width: 1200px;
    height: 751px;
    background: var(--card-bg);
    font-family: "Lato", sans-serif;
  }
  .swoosh {
    position: absolute;
    top: 0;
    left: 0;
    width: 1200px;
    height: 220px;
  }
  .brand-name {
    position: absolute;
    top: 200px;
    left: 0;
    width: 1200px;
    text-align: center;
    font-size: 64px;
    line-height: 80px;
    font-weight: 700;
    letter-spacing: 1px;
    color: var(--brand-blue);
  }
  .holder-name {
    position: absolute;
    top: 440px;
    left: 0;
    width: 1200px;
    text-align: center;
    font-size: 44px;
    line-height: 58px;
    font-weight: 400;
    color: var(--name-grey);
    letter-spacing: 0.5px;
  }
  .contact-details {
    position: absolute;
    top: 553px;
    left: 0;
    width: 1200px;
    text-align: center;
    font-size: 26px;
    line-height: 33px;
    font-style: normal;
    color: var(--text-grey);
  }
</style>
</head>
<body>
  <main class="business-card">
    <svg class="swoosh" viewBox="0 0 1200 220" aria-hidden="true">
      <defs>
        <linearGradient id="swoosh-blue" x1="0" y1="0" x2="1" y2="0">
          <stop offset="0" stop-color="#1d4f9e"/>
          <stop offset="0.5" stop-color="#3d86d0"/>
          <stop offset="1" stop-color="#1d4f9e"/>
        </linearGradient>
        <linearGradient id="swoosh-grey" x1="0" y1="0" x2="1" y2="0">
          <stop offset="0" stop-color="#8a8d91"/>
          <stop offset="0.5" stop-color="#c9cbce"/>
          <stop offset="1" stop-color="#8a8d91"/>
        </linearGradient>
      </defs>
      <path class="swoosh-blue" fill="url(#swoosh-blue)"
            d="M0 172 Q600 -80 1200 140 L1200 150 Q600 -50 0 192 Z"/>
      <path class="swoosh-grey" fill="url(#swoosh-grey)"
            d="M110 168 Q600 -20 1180 158 Q600 10 110 168 Z"/>
    </svg>

    <p class="brand-name">Horvath Law</p>

    <h1 class="holder-name">Daniel R. Horvath</h1>

    <address class="contact-details">
      <p>41756 County Lane 9 | Suite 200 | Boca Raton, FL 33517</p>
      <p>Phone: 561.472.3815 | Cell: 561.290.6174 | Fax: 561.735.9402</p>
      <p>danielrhorvath@quillpost.net | www.thedebtmender.net</p>
    </address>
  </main>
</body>
</html>
```